New Business Card Design Project

I would like my card design to look exactly like the logo, design, layout, and print of the current attached file. The only change I would like made would be for the print to say THE KMW GROUP instead of THE HALLORAN GROUP. Basically, just replace his group name with my group name. I would also like the backgroud to be the same texture and color as the attached file. I love the dark blue lettering and house logo on the card.

I am completely open to the rest of the card design. I just want something clean and simple. Only basic contact info required on the card. Maybe just name: Kyle M Warrick and cell # 555.914.2087 and email kyle@orchidhomesagent.com

```html
<!DOCTYPE html>
<html lang="en">
<head>
<meta charset="utf-8">
<title>The KMW Group – Business Card</title>
<link rel="stylesheet" href="https://fonts.googleapis.com/css2?family=PT+Sans&family=Source+Serif+4:wght@400;700&display=swap">
<style>
  :root {
    --page: #ffffff;
    --card: #d7d7d9;
    --ink: #0c0a45;
  }
  * { margin: 0; padding: 0; box-sizing: border-box; }
  html, body {
    width: 1200px;
    height: 1200px;
    overflow: hidden;
    background: var(--page);
  }
  .canvas {
    position: relative;
    width: 1200px;
    height: 1200px;
  }
  .card {
    position: absolute;
    left: 237px;
    width: 722px;
    height: 414px;
    background: var(--card);
    color: var(--ink);
  }
  .card--front { top: 155px; }
  .card--back  { top: 609px; }

  .brand-square {
    position: absolute;
    background: var(--ink);
  }
  .brand-name {
    position: absolute;
    font-family: "PT Sans", sans-serif;
    font-weight: 400;
    color: var(--ink);
    text-transform: uppercase;
  }
  .brand-name span { display: block; }

  .card--front .brand-square {
    left: 140px; top: 120px; width: 180px; height: 180px;
  }
  .card--front .brand-name {
    left: 405px; top: 122px;
    font-size: 60px; line-height: 72px;
  }

  .card--back .brand-square {
    left: 532px; top: 40px; width: 66px; height: 66px;
  }
  .card--back .brand-name {
    left: 621px; top: 36px;
    font-size: 20px; line-height: 24px;
  }

  .contact {
    position: absolute;
    left: 0; right: 0; top: 150px;
    text-align: center;
    font-family: "Source Serif 4", serif;
    color: var(--ink);
  }
  .contact__name {
    font-weight: 700;
    font-size: 31px;
    line-height: 40px;
  }
  .contact__line {
    font-weight: 400;
    font-size: 23px;
    line-height: 34px;
  }
</style>
</head>
<body>
<main class="canvas">
  <section class="card card--front" aria-label="Card front">
    <div class="brand-square"></div>
    <p class="brand-name"><span>The</span><span>KMW</span><span>Group</span></p>
  </section>

  <section class="card card--back" aria-label="Card back">
    <div class="brand-square"></div>
    <p class="brand-name"><span>The</span><span>KMW</span><span>Group</span></p>
    <div class="contact">
      <p class="contact__name">Kyle M Warrick</p>
      <p class="contact__line">555 914 2087</p>
      <p class="contact__line">kyle@orchidhomesagent.com</p>
    </div>
  </section>
</main>
</body>
</html>
```